KORVELLA Corporate Business Card

Modern business card design for company which focuses in the areas of Staffing, IT Consulting & Data Services. Please note: We are no longer using the IT subscript on the logo. All designs should have IT subscript removed.
Website: www.korvellait.example

```html
<!DOCTYPE html>
<html lang="en">
<head>
<meta charset="utf-8">
<title>KORVELLA Business Card</title>
<link rel="stylesheet" href="https://fonts.googleapis.com/css2?family=Oswald:wght@500&family=Poppins:wght@400;600&family=Roboto:wght@400&display=swap">
<style>
  :root {
    --bg: #5b5c5e;
    --card: #151617;
    --blue: #1e90dc;
    --blue-deep: #1674b8;
    --white: #f2f4f6;
  }
  * { margin: 0; padding: 0; box-sizing: border-box; }
  html, body { width: 1200px; height: 960px; overflow: hidden; background: var(--bg); }
  .canvas { position: relative; width: 1200px; height: 960px; }

  .card {
    position: absolute; left: 250px; width: 700px; height: 400px;
    background: var(--card); border-radius: 24px;
  }
  .card--front { top: 50px; }
  .card--back  { top: 500px; }
  .frame {
    position: absolute; inset: 22px;
    border: 4px solid var(--blue); border-radius: 14px;
  }

  .brand {
    position: absolute; inset: 0;
    display: flex; align-items: center; justify-content: center; gap: 18px;
  }
  .brand__mark { width: 46px; height: 46px; background: var(--blue); border-radius: 6px; }
  .brand__name {
    font-family: 'Poppins', sans-serif; font-weight: 600; font-size: 68px;
    letter-spacing: 3px; color: var(--blue);
  }

  .identity {
    position: absolute; left: 150px; top: 138px; width: 200px; text-align: right;
  }
  .identity__name {
    font-family: 'Oswald', sans-serif; font-weight: 500; font-size: 40px;
    line-height: 1; color: var(--blue); letter-spacing: 0.5px;
  }
  .identity__title {
    font-family: 'Roboto', sans-serif; font-size: 15px; color: var(--blue-deep);
    letter-spacing: 1px; margin-top: 2px;
  }
  .divider {
    position: absolute; left: 372px; top: 110px; width: 2px; height: 110px;
    background: var(--blue-deep);
  }
  .contacts {
    position: absolute; left: 394px; top: 108px; list-style: none;
    font-family: 'Roboto', sans-serif; font-size: 14.5px; color: var(--white); line-height: 1.35;
  }
  .contacts li { display: flex; align-items: flex-start; gap: 8px; }
  .contacts svg { width: 13px; height: 13px; flex: none; margin-top: 3px; fill: var(--blue); }
  .services {
    position: absolute; left: 0; right: 0; top: 300px; text-align: center;
    font-family: 'Poppins', sans-serif; font-size: 17px; color: var(--white);
  }
  .services .dot {
    display: inline-block; width: 6px; height: 6px; background: var(--blue);
    margin: 0 8px; vertical-align: middle;
  }
</style>
</head>
<body>
<main class="canvas">
  <section class="card card--front" aria-label="Card front">
    <div class="frame"></div>
    <div class="brand">
      <span class="brand__mark"></span>
      <span class="brand__name">KORVELLA</span>
    </div>
  </section>

  <section class="card card--back" aria-label="Card back">
    <div class="frame"></div>
    <div class="identity">
      <div class="identity__name">DANIEL REYES</div>
      <div class="identity__title">PRESIDENT</div>
    </div>
    <div class="divider"></div>
    <ul class="contacts">
      <li>
        <svg viewBox="0 0 24 24"><path d="M12 2a7 7 0 0 0-7 7c0 5 7 13 7 13s7-8 7-13a7 7 0 0 0-7-7zm0 9.5A2.5 2.5 0 1 1 12 6.5a2.5 2.5 0 0 1 0 5z"/></svg>
        <span>418 Harlow Ave.<br>Brookfield, IN 47199</span>
      </li>
      <li>
        <svg viewBox="0 0 24 24"><path d="M7 1h10a2 2 0 0 1 2 2v18a2 2 0 0 1-2 2H7a2 2 0 0 1-2-2V3a2 2 0 0 1 2-2zm0 3v14h10V4z"/></svg>
        <span>555-014-2290</span>
      </li>
      <li>
        <svg viewBox="0 0 24 24"><path d="M2 5h20v14H2zm2 2v.5l8 5 8-5V7z"/></svg>
        <span>contactus@korvellait.example</span>
      </li>
      <li>
        <svg viewBox="0 0 24 24"><circle cx="12" cy="12" r="10"/></svg>
        <span>www.korvellait.example</span>
      </li>
    </ul>
    <p class="services">Staffing<span class="dot"></span>IT Consulting<span class="dot"></span>Data Services</p>
  </section>
</main>
</body>
</html>
```